Lumokrit alias Jarek hat fantastische Arbeit geleistet. Zeitnahe Kommunikation, zeitnahe Umsetzung des Feedbacks und zeitnahe Bereitstellung des fertigen Projektes. Gerne jederzeit wieder.
Zielgruppe
Onlinemarketing Services für kleine und mittlere Unternehmen, wie z.B. Webseitenbau, Social Media Kampagnen oder Suchmaschinenoptimierung. Zu unseren Kunden gehören Handwerker, Tierärzte, Rechtsanwälte oder Kfz-Meisterbetriebe. Wir bedienen 6.000 Branchen von Aalräucherei bis Zylinderschleiferei, fokussieren uns aber stark auf das Handwerk.
Aufgabenstellung
Wir planen unsere Produkte unseren Kunden auf einer Plattform zur Verfügung zustellen. Hier sollen sie sich einloggen können und die Self und Managed Services nutzen können. Wir benötigen dafür eine Visualisierung. Also keine echte Webseite, sondern eine Anmutung. Sie soll nicht klickbar sein, aber sich schon wie eine fertige Webseite anfühlen.
Insgesamt sollen 3 Unterseiten gestaltet werden, die wir bereits skizziert (siehe Mockups) haben. Wir sind offen für deine Gestaltungsideen, Hauptsache es sieht nach was aus. Uns ist zudem wichtig, dass du dich bei der Farbgestaltung an der Webseite www.falvoria.com orientierst (Faust-Icon, Logo und Farbe).

```html
<!DOCTYPE html>
<html lang="de">
<head>
<meta charset="utf-8">
<title>falvoria.com – Dashboard</title>
<link href="https://fonts.googleapis.com/css2?family=Nunito+Sans:wght@400;600;700;800&display=swap" rel="stylesheet">
<style>
:root{
  --orange:#f07c00;
  --orange-soft:#f5a14b;
  --side:#666666;
  --side-dark:#575757;
  --side-line:#5a5a5a;
  --bg:#f4f4f4;
  --card:#ffffff;
  --text:#333333;
  --muted:#8a8a8a;
  --navy:#2f4a70;
  --green:#8bbf3c;
  --red:#e2402d;
  --teal:#5cc9b9;
  --btn:#a9a9a9;
  --blue-soft:#eef3f9;
}
*{box-sizing:border-box;margin:0;padding:0}
html,body{width:984px;height:1200px;overflow:hidden}
body{font-family:"Nunito Sans",sans-serif;color:var(--text);background:var(--bg);position:relative;font-size:8px}
.abs{position:absolute}
.topbar{left:0;top:0;width:984px;height:61px;background:#fff;box-shadow:0 1px 3px rgba(0,0,0,.06)}
.brand{left:17px;top:17px;display:flex;align-items:center;gap:6px;font-size:14px;font-weight:700;color:#4a4a4a}
.brand .dot{width:26px;height:26px;border-radius:50%;background:var(--orange)}
.search{left:202px;top:15px;width:162px;height:30px;border:1px solid #e6e6e6;border-radius:2px;padding:0 12px;display:flex;align-items:center;justify-content:space-between;color:#777;font-size:7px}
.quick{left:635px;top:15px;width:134px;height:29px;background:var(--orange-soft);border-radius:2px;color:#fff;font-size:9px;font-weight:700;display:flex;align-items:center;justify-content:center;gap:7px}
.notify{left:802px;top:22px}
.badge-n{left:808px;top:21px;background:var(--orange);color:#fff;font-size:6px;font-weight:700;border-radius:5px;padding:0 3px;line-height:9px}
.avatar{left:836px;top:16px;width:30px;height:30px;border-radius:50%;background:#c4c4c4}
.hello{left:877px;top:24px;font-size:11px;font-weight:700;color:#222}

.sidebar{left:0;top:61px;width:176px;height:1139px;background:var(--side-dark)}
.nav-item{position:absolute;left:0;width:176px;height:31px;display:flex;align-items:center;padding-left:20px;color:#fff;font-size:8.5px;font-weight:600;background:var(--side);border-bottom:1px solid var(--side-line)}
.nav-item svg{width:10px;height:10px;margin-right:19px;fill:#fff}
.nav-item .caret{position:absolute;right:15px;top:12px;width:0;height:0;border-left:4px solid #fff;border-top:3.5px solid transparent;border-bottom:3.5px solid transparent}
.nav-item.home{background:#f2f2f2;color:#555;border:none}
.nav-item.home svg{fill:#555}
.nav-item.active{background:var(--orange)}
.nav-item.plain{background:var(--side-dark);border-bottom:1px solid #4e4e4e}

.menu-toggle{left:205px;top:74px;width:10px}
.menu-toggle i{display:block;height:1.3px;background:#666;margin-bottom:2.4px}
.menu-toggle i:nth-child(3){width:7px}

.card{position:absolute;background:var(--card);box-shadow:0 1px 4px rgba(0,0,0,.05)}
.card-title{position:absolute;font-size:11px;font-weight:600;color:#333;display:flex;align-items:center;gap:5px}
.inner{position:absolute;background:#fff;box-shadow:0 1px 6px rgba(0,0,0,.07)}

.news .photo{height:96px;width:100%}
.news h3{font-size:9px;font-weight:400;line-height:11px;padding:12px 16px 0;color:#333}
.news p{font-size:7px;line-height:12.3px;color:#8a8a8a;padding:9px 16px 0}
.btn{display:inline-flex;align-items:center;gap:5px;background:var(--btn);color:#fff;font-size:8px;border-radius:3px;padding:0 11px;height:20px}
.news .btn{margin:7px 16px 0}
.dots{left:546px;top:118px;display:flex;gap:5px}
.dots i{width:6px;height:6px;border-radius:50%;background:#e8e8e8}
.dots i.on{background:var(--orange)}

.overview h4{font-size:10.5px;font-weight:600;padding:16px 15px 11px}
.ov-row{display:flex;align-items:center;gap:9px;padding-left:15px;height:16px;font-size:8px}
.pill{width:19px;height:9px;border-radius:5px;color:#fff;font-size:6.5px;display:flex;align-items:center;justify-content:center}

.stat .label{position:absolute;left:16px;top:16px;font-size:11.5px;font-weight:600;line-height:19px}
.stat .value{font-size:12px;font-weight:800}
.stat .note{position:absolute;left:16px;font-size:7.5px;color:#888}
.stat .mark{position:absolute;right:21px;top:17px;width:33px;height:33px;border-radius:6px;background:#e3e3e3}

.cal{left:218px;top:731px;width:192px}
.cal-head{height:23px;background:#f0f0f0;display:flex;align-items:center;justify-content:space-between;padding:0 8px;font-size:7.5px;font-weight:700}
.cal-grid{display:grid;grid-template-columns:repeat(7,1fr);font-size:7.5px;text-align:center}
.cal-grid span{height:22.4px;display:flex;align-items:center;justify-content:center;border-right:1px solid #f0f0f0;border-bottom:1px solid #f0f0f0}
.cal-grid span:nth-child(7n){border-right:none}
.cal-grid .dow{color:#666;height:20px}
.cal-grid .sun{color:var(--orange)}
.cal-grid .off{color:#ccc}
.cal-grid .sun.off{color:#f6c99a}
.cal-grid b{font-weight:400;background:var(--orange);color:#fff;width:17px;height:17px;display:flex;align-items:center;justify-content:center}

.appt{padding:17px 0 0 17px}
.appt-row{display:flex;gap:10px;font-size:8px;color:#666;line-height:9px;margin-bottom:12px}
.appt-row i{width:7px;height:7px;background:var(--orange);margin-top:1px;flex:none}

.msg h4{font-size:9.5px;font-weight:400;padding:20px 18px 0}
.msg p{font-size:7px;line-height:12.3px;color:#8a8a8a;padding:10px 18px 0}
.msg .acts{position:absolute;left:18px;bottom:16px;display:flex;gap:7px}
.icon-btn{width:20px;height:20px;background:#e4e4e4;border-radius:3px;display:flex;align-items:center;justify-content:center}

.stars{letter-spacing:.5px}
.review h4{font-size:9.5px;font-weight:400;padding:20px 20px 0}
.review .stars{padding:3px 20px 0;color:#f5b320;font-size:7px}
.review p{font-size:7px;line-height:12.3px;color:#8a8a8a;padding:6px 20px 0}
.review .btn{position:absolute;left:20px;bottom:12px}
</style>
</head>
<body>

<header class="abs topbar" aria-label="Kopfzeile"></header>
<div class="abs brand"><span class="dot"></span>falvoria.com</div>
<div class="abs search">Suchbegriff
  <svg width="9" height="9" viewBox="0 0 10 10" fill="none" stroke="#777" stroke-width="1.1"><circle cx="4" cy="4" r="3.2"/><path d="M6.4 6.4 9.3 9.3"/></svg>
</div>
<div class="abs quick">
  <svg width="14" height="13" viewBox="0 0 14 13" fill="none" stroke="#fff" stroke-width="1.1"><path d="M2 1h10a1 1 0 0 1 1 1v6a1 1 0 0 1-1 1H6l-3 3V9H2a1 1 0 0 1-1-1V2a1 1 0 0 1 1-1z"/><text x="7" y="7.5" font-size="6" fill="#fff" stroke="none" text-anchor="middle" font-family="Nunito Sans,sans-serif">?</text></svg>
  Schnellanfrage stellen
</div>
<svg class="abs notify" width="14" height="13" viewBox="0 0 14 13"><path d="M1 2h10a1 1 0 0 1 1 1v6a1 1 0 0 1-1 1H5l-3 3v-3H1a1 1 0 0 1-1-1V3a1 1 0 0 1 1-1z" fill="#555"/><rect x="2.5" y="4.5" width="7" height="1" fill="#fff"/><rect x="2.5" y="6.5" width="5" height="1" fill="#fff"/></svg>
<span class="abs badge-n">14</span>
<div class="abs avatar" role="img" aria-label="Profilbild"></div>
<div class="abs hello">Hallo, Tobias</div>

<nav class="abs sidebar" aria-label="Hauptnavigation"></nav>
<div class="nav-item home" style="top:61px;height:31px"><svg viewBox="0 0 10 10"><rect x="0" y="0" width="4.2" height="4.2" rx="1"/><rect x="5.8" y="0" width="4.2" height="4.2" rx="1"/><rect x="0" y="5.8" width="4.2" height="4.2" rx="1"/><rect x="5.8" y="5.8" width="4.2" height="4.2" rx="1"/></svg>Dashboard</div>
<div class="nav-item" style="top:92px"><svg viewBox="0 0 10 10"><rect x="1" y="1" width="9" height="8" rx="1"/><rect x="0" y="3" width="1.5" height="6"/></svg>Branchen-News<span class="caret"></span></div>
<div class="nav-item active" style="top:123.5px"><svg viewBox="0 0 10 10"><rect x="0" y="5" width="2.5" height="5"/><rect x="3.7" y="1" width="2.5" height="9"/><rect x="7.4" y="4" width="2.5" height="6"/></svg>Berichte<span class="caret"></span></div>
<div class="nav-item" style="top:155px"><svg viewBox="0 0 10 10"><ellipse cx="4" cy="4" rx="4" ry="3.3"/><ellipse cx="6.5" cy="6.3" rx="3.5" ry="3"/></svg>Chat<span class="caret"></span></div>
<div class="nav-item" style="top:186.5px"><svg viewBox="0 0 10 10"><rect x="1" y="0" width="7" height="10" rx="1"/><path d="M5 7 9.5 2.5l.5.5L5.5 7.5z" fill="#666"/></svg>Buchungen<span class="caret"></span></div>
<div class="nav-item" style="top:218px"><svg viewBox="0 0 10 10"><rect x="0" y="4" width="4" height="6"/><rect x="4.5" y="0" width="5.5" height="10"/></svg>Unternehmen<span class="caret"></span></div>
<div class="nav-item" style="top:249.5px"><svg viewBox="0 0 10 10"><rect x="0" y="1" width="10" height="8" rx="1"/><rect x="1.5" y="3" width="7" height="1" fill="#666"/><rect x="1.5" y="5" width="4" height="1" fill="#666"/></svg>Online-Profile<span class="caret"></span></div>
<div class="nav-item" style="top:281px"><svg viewBox="0 0 10 10"><circle cx="5" cy="5" r="2.2"/><circle cx="1.5" cy="1.5" r="1.3"/><circle cx="8.5" cy="1.5" r="1.3"/><rect x="4.3" y="6" width="1.4" height="4"/></svg>Bewertungen<span class="caret"></span></div>
<div class="nav-item" style="top:312.5px"><svg viewBox="0 0 10 10"><circle cx="5" cy="5" r="4.6"/><circle cx="5" cy="5" r="3" fill="#666"/><circle cx="5" cy="5" r="1.6"/></svg>SEO<span class="caret"></span></div>
<div class="nav-item" style="top:344px"><svg viewBox="0 0 10 10"><circle cx="8" cy="1.8" r="1.8"/><circle cx="2" cy="5" r="1.8"/><circle cx="8" cy="8.2" r="1.8"/><path d="M2 5 8 1.8M2 5l6 3.2" stroke="#fff" stroke-width="1"/></svg>Social Media<span class="caret"></span></div>
<div class="nav-item" style="top:375.5px"><svg viewBox="0 0 10 10"><path d="M3.5 0h3L10 8 7.8 10 5 4.5 2.2 10 0 8z"/></svg>SEA<span class="caret"></span></div>
<div class="nav-item" style="top:407px"><svg viewBox="0 0 10 10"><rect x="1.5" y="0" width="7" height="5"/><rect x="0" y="4" width="10" height="6" rx="1"/></svg>Newsletter<span class="caret"></span></div>
<div class="nav-item" style="top:438.5px"><svg viewBox="0 0 10 10"><circle cx="3.5" cy="3" r="2"/><circle cx="7.5" cy="3.5" r="1.6"/><path d="M0 9c0-2.5 1.6-3.5 3.5-3.5S7 6.5 7 9zM7.5 6c1.5 0 2.5.8 2.5 3H8z"/></svg>Recruting<span class="caret"></span></div>
<div class="nav-item" style="top:470px"><svg viewBox="0 0 10 10"><circle cx="5" cy="5" r="3.6"/><g stroke="#fff" stroke-width="1.8"><path d="M5 0v10M0 5h10M1.5 1.5l7 7M8.5 1.5l-7 7"/></g><circle cx="5" cy="5" r="1.4" fill="#666"/></svg>Einstellungen<span class="caret"></span></div>
<div class="nav-item plain" style="top:630px;border-top:1px solid #4e4e4e"><svg viewBox="0 0 10 10"><path d="M2.5 8.5a2.5 2.5 0 0 1 0-5 3 3 0 0 1 5.7.7A2.2 2.2 0 0 1 8 8.5z"/></svg>Cloud</div>
<div class="nav-item plain" style="top:660px"><svg viewBox="0 0 10 10"><circle cx="5" cy="5" r="5"/><text x="5" y="7.6" font-size="7.5" text-anchor="middle" fill="#575757" font-family="Nunito Sans,sans-serif" font-weight="800">?</text></svg>Hilfe</div>

<div class="abs menu-toggle"><i></i><i></i><i></i></div>

<!-- Branchen-News -->
<section class="card" style="left:205px;top:98px;width:740px;height:294px">
  <div class="card-title" style="left:13px;top:15px">Deine Branchen-News</div>
</section>
<div class="abs dots"><i></i><i></i><i class="on"></i></div>

<article class="inner news" style="left:218px;top:141px;width:173px;height:226px">
  <div class="photo" role="img" aria-label="Foto: gelber Schutzhelm und Arbeitshandschuhe vor einer Baustelle" style="background:linear-gradient(135deg,#9fb4c4 0%,#d9dde0 45%,#e3b23c 65%,#8d7a5e 100%)"></div>
  <h3>Azubi-Ghosting: Welche Handwerksbetriebe sind betroffen?</h3>
  <p>Ghosting: ein neuer Mitarbeiter oder neuer Auszubildender unterschreibt den Vertrag und meldet sich danach</p>
  <span class="btn"><svg width="10" height="6" viewBox="0 0 10 6"><path d="M0 3q5-6 10 0-5 6-10 0z" fill="#fff"/><circle cx="5" cy="3" r="1.4" fill="#a9a9a9"/></svg>weiterlesen</span>
</article>
<article class="inner news" style="left:403px;top:141px;width:172px;height:226px">
  <div class="photo" role="img" aria-label="Foto: Handwerker mit orangem Helm und Warnweste beim Telefonieren" style="background:linear-gradient(135deg,#4a4a48 0%,#6e6a62 40%,#d88a3a 60%,#b9c94a 100%)"></div>
  <h3>Verträge per E-Mail oder Telefon: Wann dürfen Kunden widerrufen?</h3>
  <p>Sie schließen keine Verträge ohne einen Ortstermin oder ein Gespräch Auge in Auge mit dem Kunden ab?</p>
  <span class="btn"><svg width="10" height="6" viewBox="0 0 10 6"><path d="M0 3q5-6 10 0-5 6-10 0z" fill="#fff"/><circle cx="5" cy="3" r="1.4" fill="#a9a9a9"/></svg>weiterlesen</span>
</article>
<div class="abs" role="img" aria-label="Illustration: Person am Laptop mit Symbolen für Einstellungen, Statistik und Unternehmen" style="left:592px;top:162px;width:164px;height:212px;border-radius:50% 50% 40% 40%/30% 30% 12% 12%;background:radial-gradient(ellipse at 50% 60%,#f6d2ad 0%,#eef0f3 55%,#ffffff 80%)"></div>

<aside class="inner overview" style="left:774px;top:141px;width:158px;height:233px">
  <div style="background:var(--blue-soft);height:115px">
    <h4>Deine Kurzübersicht</h4>
    <div class="ov-row"><span class="pill" style="background:var(--orange)">11</span>neue Aufträge</div>
    <div class="ov-row"><span class="pill" style="background:#a6cc5a">5</span>neue Bewertungen</div>
    <div class="ov-row"><span class="pill" style="background:var(--teal)">27</span>neue Nachrichten</div>
  </div>
  <div role="img" aria-label="Foto der Ansprechpartnerin" style="width:38px;height:38px;border-radius:50%;background:linear-gradient(#f0d8b8,#c9a27a);margin:14px auto 0"></div>
  <div style="text-align:center;font-size:9px;margin-top:10px">Lena Brückmann</div>
  <div style="text-align:center;font-size:7.5px;color:#888;margin-top:2px">Service &amp; Support</div>
  <div style="display:flex;justify-content:center;align-items:center;gap:5px;margin-top:6px;color:var(--navy);font-size:9.5px;font-weight:600">
    <svg width="13" height="11" viewBox="0 0 13 11"><ellipse cx="6.5" cy="5" rx="6" ry="4.5" fill="var(--navy)"/><path d="M4 9.5 2.5 11l3-1.5z" fill="var(--navy)"/><circle cx="4" cy="5" r=".8" fill="#fff"/><circle cx="6.5" cy="5" r=".8" fill="#fff"/><circle cx="9" cy="5" r=".8" fill="#fff"/></svg>
    +49 221 555 04 17
  </div>
</aside>

<!-- Berichte -->
<section class="card" style="left:205px;top:421px;width:370px;height:235px">
  <svg width="370" height="235" viewBox="362 743 653 414" font-family="Nunito Sans,sans-serif">
    <g fill="#333"><rect x="386" y="780" width="3" height="9"/><rect x="391" y="775" width="3" height="14"/><rect x="396" y="778" width="3" height="11"/></g>
    <text x="408" y="789" font-size="19" fill="#333" font-weight="600">Deine Berichte</text>
    <g font-size="12" fill="#555">
      <text x="384" y="841">100k</text><text x="386" y="890">80k</text><text x="386" y="939">60k</text><text x="386" y="985">40k</text><text x="386" y="1030">20k</text><text x="393" y="1078">0</text>
    </g>
    <g stroke="#eee" stroke-width="1">
      <path d="M439 833v248M524 833v248M609 833v248M781 833v248M866 833v248M953 833v248"/>
      <path d="M430 1081h525"/>
    </g>
    <path d="M696 833v248" stroke="#bbb" stroke-dasharray="4 4"/>
    <polyline fill="none" stroke="#f7941d" stroke-width="3" points="433,1057 472,1040 525,1062 572,1032 628,1050 670,994 752,1052 805,1024 857,1052 917,1020 950,1024"/>
    <polyline fill="none" stroke="#2f4a70" stroke-width="3" points="433,970 472,1000 508,982 545,1018 625,996 696,938 743,902 765,980 835,1002 867,934 920,984 949,882"/>
    <circle cx="696" cy="938" r="8" fill="#f07c00"/>
    <rect x="552" y="872" width="115" height="68" rx="6" fill="#5a5a5a"/>
    <path d="M667 920l10 10-14 0z" fill="#5a5a5a"/>
    <text x="575" y="901" font-size="15" fill="#fff" font-weight="600">Webseite</text>
    <text x="575" y="922" font-size="11" fill="#fff">18. Aug., 2022</text>
    <g fill="#fff" stroke="#bbb" stroke-width="1.3">
      <circle cx="439" cy="1094" r="4"/><circle cx="524" cy="1094" r="4"/><circle cx="609" cy="1094" r="4"/><circle cx="779" cy="1094" r="4"/><circle cx="864" cy="1094" r="4"/><circle cx="949" cy="1094" r="4"/>
    </g>
    <circle cx="694" cy="1094" r="4" fill="#bbb"/>
    <g font-size="13" fill="#333" font-weight="600" text-anchor="middle">
      <text x="439" y="1122">MO</text><text x="524" y="1122">DI</text><text x="609" y="1122">MI</text><text x="695" y="1122">DO</text><text x="779" y="1122">FR</text><text x="865" y="1122">SA</text><text x="950" y="1122">SO</text>
    </g>
  </svg>
</section>

<div class="card stat" style="left:588px;top:421px;width:172px;height:110px;background:linear-gradient(180deg,#2f4a70 0%,#4d6a91 100%);color:#fff">
  <div class="label">Webseite<br><span class="value">+20%</span></div>
  <svg class="abs" style="right:20px;top:17px" width="38" height="33" viewBox="0 0 38 33" fill="none" stroke="#fff" stroke-width="2"><rect x="1" y="1" width="36" height="31" rx="2" fill="#fff" fill-opacity=".08"/><path d="M1 8h36"/><circle cx="5" cy="4.5" r="1.3"/><circle cx="9.5" cy="4.5" r="1.3"/><circle cx="14" cy="4.5" r="1.3"/><rect x="5" y="13" width="12" height="14"/><path d="M21 14h12M21 20h12M21 26h12"/></svg>
  <div class="note" style="top:79px;color:#fff">+0,5% zur Vorwoche</div>
</div>
<div class="card stat" style="left:774px;top:421px;width:171px;height:110px">
  <div class="label">Findora<br><span class="value" style="color:var(--green)">+240%</span></div>
  <span class="mark"></span>
  <div class="note" style="top:80px">+25,1% zur Vorwoche</div>
</div>
<div class="card stat" style="left:588px;top:545px;width:172px;height:111px">
  <div class="label" style="left:18px;top:17px">Socialo<br><span class="value" style="color:var(--green)">+120%</span></div>
  <span class="mark"></span>
  <div class="note" style="left:18px;top:83px">+12,1% zur Vorwoche</div>
</div>
<div class="card stat" style="left:774px;top:545px;width:171px;height:111px">
  <div class="label" style="top:18px">Fotogram<br><span class="value" style="color:var(--red)">-5%</span></div>
  <span class="mark"></span>
  <div class="note" style="top:84px">-7,8% zur Vorwoche</div>
</div>

<!-- Terminanfragen -->
<section class="card" style="left:205px;top:684px;width:370px;height:236px">
  <div class="card-title" style="left:13px;top:16px">
    <svg width="10" height="10" viewBox="0 0 10 10" fill="none" stroke="#333" stroke-width="1.1"><rect x=".6" y="1.6" width="8.8" height="7.8" rx="1"/><path d="M.6 4h8.8M3 .3v2.5M7 .3v2.5"/></svg>Terminanfragen
  </div>
</section>
<div class="abs cal">
  <div class="cal-head"><span>◂</span>Dezember 2022<span>▸</span></div>
  <div class="cal-grid">
    <span class="dow">Mo</span><span class="dow">Di</span><span class="dow">Mi</span><span class="dow">Do</span><span class="dow">Fr</span><span class="dow">Sa</span><span class="dow sun">So</span>
    <span class="off">30</span><span>1</span><span><b>2</b></span><span>3</span><span><b>4</b></span><span>5</span><span class="sun">6</span>
    <span>7</span><span>8</span><span>9</span><span>10</span><span>11</span><span>12</span><span class="sun">13</span>
    <span>14</span><span><b>15</b></span><span>16</span><span>17</span><span>18</span><span>19</span><span class="sun">20</span>
    <span>21</span><span>22</span><span>23</span><span>24</span><span>25</span><span>26</span><span class="sun">27</span>
    <span>28</span><span>29</span><span>30</span><span class="off">31</span><span class="off">1</span><span class="off">2</span><span class="sun off">3</span>
  </div>
</div>
<div class="inner appt" style="left:429px;top:731px;width:131px;height:115px">
  <div class="appt-row"><i></i><div>Mittwoch, 02.12.2022<br>14:00 - 14:30 Uhr</div></div>
  <div class="appt-row"><i></i><div>Freitag, 04.12.2022<br>08:00 - 10:15 Uhr</div></div>
  <div class="appt-row"><i></i><div>Dienstag, 15.12.2022<br>09:00 - 09:30 Uhr</div></div>
</div>

<!-- Chatnachrichten -->
<section class="card" style="left:588px;top:684px;width:357px;height:236px">
  <div class="card-title" style="left:22px;top:16px">
    <svg width="9" height="9" viewBox="0 0 9 9"><path d="M1 0h7a1 1 0 0 1 1 1v5a1 1 0 0 1-1 1H4L1.5 9V7H1a1 1 0 0 1-1-1V1a1 1 0 0 1 1-1z" fill="#333"/><rect x="2" y="2" width="5" height=".9" fill="#fff"/><rect x="2" y="4" width="3.5" height=".9" fill="#fff"/></svg>Chatnachrichten
  </div>
</section>
<article class="inner msg" style="left:601px;top:729px;width:158px;height:170px">
  <h4>Anfrage Sanierung</h4>
  <p>Überall dieselbe alte Leier. Das Layout ist fertig, der Text lässt auf sich warten. Damit das Layout nun nicht nackt im Raume steht und sich klein und leer vorkommt, springe ich ein:</p>
  <div class="acts"><span class="btn"><svg width="10" height="6" viewBox="0 0 10 6"><path d="M0 3q5-6 10 0-5 6-10 0z" fill="#fff"/><circle cx="5" cy="3" r="1.4" fill="#a9a9a9"/></svg>anzeigen</span><span class="icon-btn"><svg width="11" height="8" viewBox="0 0 11 8" fill="none" stroke="#888"><rect x=".5" y=".5" width="10" height="7"/><path d="M.5.5 5.5 4.5 10.5.5M.5 7.5l4-3.5M10.5 7.5l-4-3.5"/></svg></span></div>
</article>
<article class="inner msg" style="left:774px;top:729px;width:158px;height:170px">
  <h4 style="padding-top:18px">RE: Vielen lieben Dank</h4>
  <p>Überall dieselbe alte Leier. Das Layout ist fertig, der Text lässt auf sich warten. Damit das Layout nun nicht nackt im Raume steht und sich klein und leer vorkommt, springe ich ein:</p>
  <div class="acts" style="bottom:17px"><span class="btn"><svg width="10" height="6" viewBox="0 0 10 6"><path d="M0 3q5-6 10 0-5 6-10 0z" fill="#fff"/><circle cx="5" cy="3" r="1.4" fill="#a9a9a9"/></svg>anzeigen</span><span class="icon-btn"><svg width="11" height="8" viewBox="0 0 11 8" fill="none" stroke="#888"><rect x=".5" y=".5" width="10" height="7"/><path d="M.5.5 5.5 4.5 10.5.5M.5 7.5l4-3.5M10.5 7.5l-4-3.5"/></svg></span></div>
</article>

<!-- Bewertungen -->
<section class="card" style="left:205px;top:948px;width:740px;height:214px"></section>
<div class="inner" style="left:218px;top:993px;width:357px;height:150px">
  <div class="abs" style="left:22px;top:23px;font-size:9px">Kundenzufriedenheit</div>
  <div class="abs" style="left:22px;top:41px;color:var(--green);font-size:17px;font-weight:800">4,7 <span style="font-size:8px;font-weight:400">von 5</span></div>
  <div class="abs stars" style="left:21px;top:64px;color:var(--green);font-size:17px;letter-spacing:0">★★★★★</div>
  <div class="abs" style="left:22px;top:97px;color:var(--green);font-size:7.5px;font-weight:700;letter-spacing:.3px">EMPFEHLENSWERT</div>
  <div class="abs" style="left:22px;top:119px;color:#888;font-size:7.5px">27 Bewertungen</div>
  <div class="abs" style="left:194px;top:23px;font-size:9px">Anzahl der Sterne-Bewertungen</div>
  <div class="abs" style="left:194px;top:42px;font-size:11px;line-height:16.6px;letter-spacing:0">
    <div><span style="color:#5cc9a0">★★★★★</span> <span style="color:#888;font-size:8px;margin-left:6px">13</span></div>
    <div><span style="color:#a6cc5a">★★★★</span><span style="color:#e6e6e6">★</span> <span style="color:#888;font-size:8px;margin-left:6px">8</span></div>
    <div><span style="color:#f5c030">★★★</span><span style="color:#e6e6e6">★★</span> <span style="color:#888;font-size:8px;margin-left:6px">3</span></div>
    <div><span style="color:#f39a2b">★★</span><span style="color:#e6e6e6">★★★</span> <span style="color:#888;font-size:8px;margin-left:6px">1</span></div>
    <div><span style="color:#f26b5b">★</span><span style="color:#e6e6e6">★★★★</span> <span style="color:#888;font-size:8px;margin-left:6px">0</span></div>
  </div>
</div>
<article class="inner review" style="left:600px;top:993px;width:159px;height:150px">
  <h4>Sehr zufrieden, wie immer!</h4>
  <div class="stars">★★★★★</div>
  <p>Überall dieselbe alte Leier. Das Layout ist fertig, der Text lässt auf sich warten. Damit das Layout nun nicht nackt im Raume steht und sich klein und leer vorkommt.</p>
  <span class="btn">antworten <svg width="11" height="8" viewBox="0 0 11 8" fill="none" stroke="#fff"><rect x=".5" y=".5" width="10" height="7"/><path d="M.5.5 5.5 4.5 10.5.5"/></svg></span>
</article>
<article class="inner review" style="left:774px;top:993px;width:158px;height:150px">
  <h4>Spitzenmäßige Leistung</h4>
  <div class="stars">★★★★★</div>
  <p>Überall dieselbe alte Leier. Das Layout ist fertig, der Text lässt auf sich warten. Damit das Layout nun nicht nackt im Raume steht und sich klein und leer vorkommt.</p>
  <span class="btn">antworten <svg width="11" height="8" viewBox="0 0 11 8" fill="none" stroke="#fff"><rect x=".5" y=".5" width="10" height="7"/><path d="M.5.5 5.5 4.5 10.5.5"/></svg></span>
</article>

</body>
</html>
```